Design a Personable Book Cover for Youth Written by a Teenager

We are looking for a talented designer that understands the youth.
This book is full of poems of a high school student coping with the struggles of that age group 14 year old to 17 years old.

We need a book cover with back cover and spine done.
But, first we want to get the front cover part.
For the front cover we want the picture of the author (attached), the title, and author's name.

Also, we want the red logo (attached) we want it on the sleeve of the author's shirt. We will provide the details for spine and back cover after we get the front cover done.

Book size: 5.5inX8.5in
Author name: Marisol Quintero
Book title: A Restless Season

If you consider yourself a talented designer and are up for the challenge.
Please reach out with any questions.

Thank you we appreciate you!

Target Market(s)

Youth in school, Middle to High School

Industry/Entity Type

Education

Font styles to use
Script

Colors
ffffff

Requirements
Must have
• Picture of author in front with logo in her shirt's sleeve
Should not have
• Anything that can be appropiate by shools

```html
<!DOCTYPE html>
<html lang="en">
<head>
<meta charset="utf-8">
<title>A Restless Season — Cover Set</title>
<link href="https://fonts.googleapis.com/css2?family=Montserrat:wght@500;700;900&family=Oswald:wght@700&display=swap" rel="stylesheet">
<style>
  :root {
    --stage-light: #c4c6c8;
    --stage-dark: #7f8285;
    --paper: #ffffff;
    --ink-red: #d5162b;
    --photo-red: #c7321f;
    --photo-amber: #e3b21a;
    --photo-brown: #5a3a22;
    --back-charcoal: #3c3a3a;
    --back-title: #d9d9d9;
    --back-copy: #bdbdbd;
    --strip-teal: #2f8f7a;
    --strip-olive: #9a9a3a;
  }
  * { margin: 0; padding: 0; box-sizing: border-box; }
  html, body { width: 1200px; height: 900px; overflow: hidden; }
  body {
    background: radial-gradient(ellipse at 50% 45%, var(--stage-light) 0%, var(--stage-dark) 100%);
    font-family: "Montserrat", Arial, sans-serif;
    position: relative;
  }

  .cover {
    position: absolute;
    top: 90px;
    width: 466px;
    height: 720px;
    overflow: hidden;
    box-shadow: 0 18px 40px rgba(0,0,0,0.35);
  }
  .cover--front { left: 94px; background: var(--paper); }
  .cover--back { left: 640px; background: var(--back-charcoal); }

  /* Front cover */
  .front-photo {
    position: absolute;
    left: 0; top: 110px;
    width: 380px; height: 610px;
    background:
      radial-gradient(ellipse at 40% 30%, rgba(255,255,255,0.55) 0%, rgba(255,255,255,0) 45%),
      linear-gradient(170deg, var(--photo-red) 0%, #b5462a 35%, var(--photo-brown) 60%, var(--photo-amber) 85%, #f2d46a 100%);
  }
  .front-spray {
    position: absolute;
    left: 120px; top: 40px;
    width: 346px; height: 330px;
    background: radial-gradient(ellipse at 40% 40%, rgba(213,22,43,0.28) 0%, rgba(213,22,43,0.1) 45%, rgba(213,22,43,0) 70%);
  }
  .publisher-mark {
    position: absolute;
    right: 34px; top: 40px;
    display: flex; align-items: center; gap: 7px;
    color: var(--ink-red);
    font-weight: 700;
    font-size: 13px;
    letter-spacing: 0.5px;
  }
  .publisher-mark__dot {
    width: 12px; height: 12px;
    border-radius: 50%;
    background: var(--ink-red);
  }
  .front-title {
    position: absolute;
    left: 140px; top: 300px;
    width: 300px;
    color: var(--ink-red);
    font-family: "Oswald", "Montserrat", sans-serif;
    font-weight: 700;
    text-transform: uppercase;
    line-height: 0.92;
    white-space: nowrap;
  }
  .front-title__lead { display: block; font-size: 28px; }
  .front-title__word { display: block; font-size: 62px; letter-spacing: 0.5px; }
  .front-author {
    position: absolute;
    right: 34px; top: 548px;
    color: var(--ink-red);
    font-weight: 900;
    font-size: 22px;
    text-transform: uppercase;
    letter-spacing: 0.5px;
    white-space: nowrap;
  }

  /* Back cover */
  .back-facets {
    position: absolute; inset: 0;
    width: 100%; height: 100%;
  }
  .back-strip-top {
    position: absolute;
    left: 0; top: 0;
    width: 100%; height: 48px;
    background: linear-gradient(90deg, var(--paper) 0%, #e8efe9 40%, var(--strip-teal) 70%, var(--paper) 100%);
  }
  .back-strip-side {
    position: absolute;
    right: 0; top: 48px;
    width: 150px; height: 672px;
    background: linear-gradient(180deg, var(--paper) 0%, #dfe6dc 20%, var(--strip-teal) 45%, var(--strip-olive) 70%, var(--paper) 100%);
  }
  .back-title {
    position: absolute;
    left: 36px; top: 92px;
    color: var(--back-title);
    font-family: "Oswald", "Montserrat", sans-serif;
    font-weight: 700;
    text-transform: uppercase;
    line-height: 0.95;
  }
  .back-title__lead { display: block; font-size: 15px; }
  .back-title__word { display: block; font-size: 32px; }
  .back-blurb {
    position: absolute;
    left: 36px; top: 190px;
    width: 250px;
    color: var(--back-copy);
    font-size: 11.5px;
    line-height: 1.55;
    font-weight: 500;
  }
  .back-mark {
    position: absolute;
    left: 110px; bottom: 44px;
    display: flex; align-items: center; gap: 6px;
    color: var(--ink-red);
    font-weight: 700;
    font-size: 11px;
  }
  .back-mark__dot {
    width: 10px; height: 10px;
    border-radius: 50%;
    background: var(--ink-red);
  }
</style>
</head>
<body>

  <section class="cover cover--front" aria-label="Front cover">
    <div class="front-spray"></div>
    <div class="front-photo" role="img" aria-label="Duotone portrait of the author in a cap and T-shirt, with the publisher mark on her sleeve"></div>
    <div class="publisher-mark"><span class="publisher-mark__dot"></span>Restless Press</div>
    <h1 class="front-title">
      <span class="front-title__lead">A</span>
      <span class="front-title__word">Restless</span>
      <span class="front-title__word">Season</span>
    </h1>
    <p class="front-author">Marisol Quintero</p>
  </section>

  <section class="cover cover--back" aria-label="Back cover">
    <svg class="back-facets" viewBox="0 0 466 720" preserveAspectRatio="none" aria-hidden="true">
      <polygon points="0,0 200,0 90,260" fill="#454343"/>
      <polygon points="90,260 200,0 320,300" fill="#4c4a4a"/>
      <polygon points="0,0 90,260 0,420" fill="#3f3d3d"/>
      <polygon points="0,420 90,260 220,520" fill="#484646"/>
      <polygon points="90,260 320,300 220,520" fill="#535151"/>
      <polygon points="0,420 220,520 0,720" fill="#363434"/>
      <polygon points="220,520 320,300 466,720 0,720" fill="#3a3838"/>
    </svg>
    <div class="back-strip-top" role="img" aria-label="Cropped photo detail along the top edge"></div>
    <div class="back-strip-side" role="img" aria-label="Cropped photo of the author's arm and sleeve in teal and olive tones"></div>
    <h2 class="back-title">
      <span class="back-title__lead">A</span>
      <span class="back-title__word">Restless</span>
      <span class="back-title__word">Season</span>
    </h2>
    <p class="back-blurb">Some days the halls feel louder than my own thoughts, and some nights the quiet is worse. These poems were written between classes, on bus rides, in the margins of homework I never finished. They are about friends who drift, parents who try, mirrors that lie, and the stubborn hope that keeps showing up anyway. If you have ever felt too much and too little at the same time, this book is for you. Read it slowly. Read it out loud. Then write your own season down before it passes.</p>
    <div class="back-mark"><span class="back-mark__dot"></span>Restless Press</div>
  </section>

</body>
</html>
```